Corvant Systems Business Card

Create an appealing and elegant Business card for corvant systems. Include logo and use related colors from website, be creative. Include Business name, my name, tile, address, contacts, address, and social media contacts if possible. Logo PSD file is attached.

Bleed Area: 3.46" x 2.32"
Trim: 3.3" x 2.16"
Safe Area: 3.14" x 2.02"

Save files as vector-based PDF with outlined text and PNG.
No crop marks
CMYK color setting

Business Card Info:

Corvant Systems

Dennis Halvorsen
Owner

512 Brindlemoor Rd Unit C
Ashmere Bay, CV 02871
t. 1.888.555.0162
e. dennis.h@corvantsys.example
w. www.corvantsys.example

facebook. www.pagebook.example/CorvantSys
twitter. chirpline.example/corvantsys
pinterest. www.pinboardly.example/corvantsys/

Target Market(s)

Business Owners and Partners

Industry/Entity Type

Business

Requirements
Must have
• Logo and related colors from website

```html
<!DOCTYPE html>
<html lang="en">
<head>
<meta charset="utf-8">
<title>Corvant Systems – Business Card</title>
<link rel="stylesheet" href="https://fonts.googleapis.com/css2?family=Open+Sans:wght@400&display=swap">
<style>
  :root {
    --paper: #ffffff;
    --accent-orange: #f2a225;
    --panel-grey-dark: #76716a;
    --panel-grey-light: #a29d90;
    --panel-blue: #7098cb;
    --panel-blue-light: #86a9d6;
    --icon-blue: #5a82bd;
    --ink: #111111;
    --on-panel: #ffffff;
  }
  html, body {
    margin: 0;
    padding: 0;
    width: 1200px;
    height: 786px;
    overflow: hidden;
    background: var(--paper);
  }
  .card {
    position: relative;
    width: 1200px;
    height: 786px;
    overflow: hidden;
    background: var(--paper);
    font-family: "Open Sans", sans-serif;
  }
  .card-shapes {
    position: absolute;
    inset: 0;
  }
  .wordmark {
    position: absolute;
    left: 74px;
    top: 150px;
    color: var(--ink);
    font-weight: 400;
    line-height: 1;
  }
  .wordmark-line {
    display: block;
    white-space: nowrap;
  }
  .wordmark-primary { font-size: 116px; letter-spacing: 2px; }
  .wordmark-secondary { font-size: 76px; margin-top: 14px; letter-spacing: 1px; }

  .holder {
    position: absolute;
    right: 59px;
    top: 88px;
    text-align: right;
    color: var(--on-panel);
    line-height: 1;
  }
  .holder-name { font-size: 45px; display: block; }
  .holder-title { font-size: 33px; display: block; margin-top: 2px; }

  .contact {
    position: absolute;
    left: 705px;
    top: 262px;
    margin: 0;
    padding: 0;
    list-style: none;
    color: var(--on-panel);
    font-size: 28px;
    line-height: 38px;
    white-space: nowrap;
  }

  .social {
    position: absolute;
    left: 90px;
    top: 555px;
    margin: 0;
    padding: 0;
    list-style: none;
    color: var(--on-panel);
    font-size: 29px;
    white-space: nowrap;
  }
  .social-item {
    display: flex;
    align-items: center;
    height: 49px;
  }
  .social-dot {
    width: 38px;
    height: 38px;
    border-radius: 50%;
    background: var(--icon-blue);
    margin-right: 6px;
    flex: none;
  }
</style>
</head>
<body>
<div class="card">
  <svg class="card-shapes" width="1200" height="786" viewBox="0 0 1200 786" aria-hidden="true">
    <defs>
      <linearGradient id="grey-panel" x1="0" y1="1" x2="1" y2="0">
        <stop offset="0" stop-color="var(--panel-grey-dark)"/>
        <stop offset="1" stop-color="var(--panel-grey-light)"/>
      </linearGradient>
      <linearGradient id="blue-panel" x1="0" y1="1" x2="1" y2="0">
        <stop offset="0" stop-color="var(--panel-blue)"/>
        <stop offset="1" stop-color="var(--panel-blue-light)"/>
      </linearGradient>
    </defs>
    <polygon class="corner-accent" points="0,0 244,0 0,140" fill="var(--accent-orange)"/>
    <polygon class="panel-contact" points="589,194 925,0 1200,0 1200,484 790,716 589,358" fill="url(#grey-panel)"/>
    <polygon class="panel-social" points="0,534 288,368 578,368 781,723 677,786 0,786" fill="url(#grey-panel)"/>
    <polygon class="panel-services" points="1200,502 716,786 1200,786" fill="url(#blue-panel)"/>

    <g class="contact-icon" transform="translate(677,277)">
      <circle r="19" fill="var(--icon-blue)"/>
      <rect x="-11" y="-7" width="22" height="14" rx="2" fill="#fff"/>
      <polyline points="-11,-6 0,2 11,-6" fill="none" stroke="var(--icon-blue)" stroke-width="2"/>
    </g>

    <g class="service-icons" fill="rgba(255,255,255,0.12)" stroke="rgba(255,255,255,0.7)" stroke-width="1.5">
      <circle cx="976" cy="730" r="41"/>
      <circle cx="1055" cy="685" r="41"/>
      <circle cx="1131" cy="640" r="41"/>
    </g>
    <g class="icon-design" transform="translate(976,730)" fill="#fff">
      <ellipse cx="0" cy="0" rx="17" ry="13"/>
      <circle cx="-6" cy="-4" r="2.5" fill="var(--panel-blue)"/>
      <circle cx="2" cy="-6" r="2.5" fill="var(--panel-blue)"/>
      <circle cx="8" cy="0" r="2.5" fill="var(--panel-blue)"/>
    </g>
    <g class="icon-search" transform="translate(1055,685)" fill="none" stroke="#fff" stroke-width="4" stroke-linecap="round">
      <circle cx="-3" cy="-3" r="8"/>
      <line x1="3" y1="3" x2="11" y2="9"/>
    </g>
    <g class="icon-laptop" transform="translate(1131,640) rotate(-25)" fill="none" stroke="#fff" stroke-width="3" stroke-linejoin="round">
      <rect x="-15" y="-12" width="30" height="20" rx="2"/>
      <line x1="-19" y1="12" x2="19" y2="12"/>
    </g>
  </svg>

  <div class="wordmark" aria-label="Corvant Systems">
    <span class="wordmark-line wordmark-primary">Corvant</span>
    <span class="wordmark-line wordmark-secondary">Systems</span>
  </div>

  <div class="holder">
    <span class="holder-name">Dennis Halvorsen</span>
    <span class="holder-title">Owner</span>
  </div>

  <ul class="contact">
    <li class="contact-line">512 Brindlemoor Rd Unit C</li>
    <li class="contact-line">Ashmere Bay, CV 02871</li>
    <li class="contact-line">t. 1.888.555.0162</li>
    <li class="contact-line">e. dennis.h@corvantsys.example</li>
    <li class="contact-line">w. www.corvantsys.example</li>
  </ul>

  <ul class="social">
    <li class="social-item"><span class="social-dot"></span>www.pagebook.example/CorvantSys</li>
    <li class="social-item"><span class="social-dot"></span>chirpline.example/corvantsys</li>
    <li class="social-item"><span class="social-dot"></span>www.pinboardly.example/corvantsys/</li>
  </ul>
</div>
</body>
</html>
```